Commercial facility maintenance

I need a card design that helps my salesmen make contact with new clients, our product is facility maintenance and heavy industrial maintenance

```html
<!DOCTYPE html>
<html lang="en">
<head>
<meta charset="utf-8">
<title>Halvorsen Millworks LLC – Business Card</title>
<link rel="stylesheet" href="https://fonts.googleapis.com/css2?family=Poppins:ital,wght@0,400;0,500;0,600;0,700;1,400&display=swap">
<style>
  :root{
    --page:#ffffff;
    --card:#252729;
    --card-deep:#1f2123;
    --red:#d2232a;
    --red-deep:#8f1218;
    --white:#ffffff;
    --photo-light:#8c8f93;
    --photo-dark:#3a3d40;
  }
  *{box-sizing:border-box;margin:0;padding:0}
  html,body{width:923px;height:1200px;overflow:hidden;background:var(--page)}
  body{position:relative;font-family:"Poppins",sans-serif;color:var(--white)}

  .card{
    position:absolute;left:62px;width:798px;height:456px;
    background:radial-gradient(ellipse at 70% 30%, #2b2d2f 0%, var(--card) 55%, var(--card-deep) 100%);
    box-shadow:0 14px 22px rgba(0,0,0,.35);
    overflow:hidden;
  }
  .card--front{top:97px}
  .card--back{top:600px;border-right:2px solid var(--red)}

  /* front */
  .brand{
    position:absolute;left:0;right:0;top:150px;height:56px;
    display:flex;align-items:center;justify-content:center;gap:12px;
  }
  .brand__mark{width:52px;height:52px;border-radius:50%;background:var(--red);flex:none}
  .brand__name{font-weight:700;font-size:24px;letter-spacing:.5px;line-height:1;color:var(--white);white-space:nowrap}

  .service{
    position:absolute;left:116px;width:567px;height:55px;
    border:2px solid var(--red);border-radius:28px;background:var(--red-deep);
    display:flex;align-items:center;justify-content:center;
    font-weight:600;font-size:20px;letter-spacing:3.4px;white-space:nowrap;
  }
  .service--commercial{top:275px}
  .service--industrial{top:340px}

  /* back */
  .portrait{
    position:absolute;left:0;top:15px;width:385px;height:441px;
    background:linear-gradient(180deg,var(--photo-dark) 0%,var(--photo-light) 55%,#6e7175 100%);
    clip-path:polygon(75px 0,235px 0,255px 120px,250px 225px,335px 270px,365px 300px,385px 441px,0 441px,0 270px,45px 240px,75px 200px,70px 60px);
  }
  .baseline{position:absolute;left:385px;right:0;bottom:0;height:2px;background:var(--red)}

  .name{
    position:absolute;left:285px;top:86px;width:415px;height:62px;
    border:2px solid var(--red);border-radius:32px;background:var(--red-deep);
    display:flex;align-items:center;justify-content:center;gap:10px;
    font-size:31px;letter-spacing:-.3px;white-space:nowrap;
  }
  .name__first{font-weight:700}
  .name__last{font-weight:400}

  .role{
    position:absolute;left:288px;top:156px;
    font-style:italic;font-size:18px;line-height:23px;
  }
  .divider{position:absolute;left:291px;top:228px;width:459px;border-top:1.5px dashed var(--red)}

  .contact{position:absolute;left:388px;display:flex;align-items:center;font-size:19px;white-space:nowrap}
  .contact svg{width:20px;height:20px;margin-right:14px;flex:none}
  .contact--phone{top:278px}
  .contact--mail{top:325px}
  .contact--web{top:372px}
</style>
</head>
<body>

<section class="card card--front">
  <div class="brand">
    <span class="brand__mark"></span>
    <span class="brand__name">HALVORSEN MILLWORKS LLC</span>
  </div>
  <div class="service service--commercial">COMMERCIAL FACILITY MAINTENANCE</div>
  <div class="service service--industrial">HEAVY INDUSTRIAL MAINTENANCE</div>
</section>

<section class="card card--back">
  <div class="portrait" role="img" aria-label="Portrait photo of the specialist in a grey suit"></div>
  <div class="baseline"></div>

  <div class="name"><span class="name__first">DANIEL</span><span class="name__last">MARLOWE</span></div>
  <p class="role">Specialist,<br>Heavy industrial maintenance</p>
  <div class="divider"></div>

  <div class="contact contact--phone">
    <svg viewBox="0 0 24 24" aria-hidden="true"><path fill="#d2232a" d="M6.6 10.8a15.1 15.1 0 0 0 6.6 6.6l2.2-2.2c.3-.3.7-.4 1-.2 1.1.4 2.3.6 3.6.6.6 0 1 .4 1 1V20c0 .6-.4 1-1 1A17 17 0 0 1 3 4c0-.6.4-1 1-1h3.5c.6 0 1 .4 1 1 0 1.2.2 2.4.6 3.6.1.3 0 .7-.2 1z"/><path fill="none" stroke="#d2232a" stroke-width="1.6" d="M14 3.5a7 7 0 0 1 6.5 6.5M14 7a3.5 3.5 0 0 1 3 3"/></svg>
    <span>555-014-2280</span>
  </div>
  <div class="contact contact--mail">
    <svg viewBox="0 0 24 24" aria-hidden="true"><rect x="2" y="5" width="20" height="14" fill="#d2232a"/><path d="M2 5l10 8 10-8M2 19l7-7M22 19l-7-7" fill="none" stroke="#252729" stroke-width="1.4"/></svg>
    <span>daniel@halvorsenmillworks.com</span>
  </div>
  <div class="contact contact--web">
    <svg viewBox="0 0 24 24" aria-hidden="true"><circle cx="12" cy="12" r="10" fill="#d2232a"/><path d="M2 12h20M12 2v20M4 7h16M4 17h16M12 2c-4 4-4 16 0 20M12 2c4 4 4 16 0 20" fill="none" stroke="#252729" stroke-width="1.2"/></svg>
    <span>www.halvorsenmillworks.com</span>
  </div>
</section>

</body>
</html>
```